Land Buying Company Needs Letterhead for Direct Mail Marketing to Land Owners

We are looking for a professional letterhead that we will be including in our direct mail marketing. We will be sending this to land owners who may be interested in selling or purchasing land.

The letterhead needs to be editable. Headers and footers would look nice, but we are open. We would want it to include our address, website, phone, and email info. For right now the address to use for design purposes would the following:

Address: 415 Bramwell Avenue #600
Dallas, TX 75219
Website - www.quillridgeacres.example
Email - info@quillridgeacres.example
Phone - 866-402-ACRE

I have attached our logo zip file that we just had done on Pixel Guild. Let me know what questions you have, and thank you.

```html
<!DOCTYPE html>
<html lang="en">
<head>
<meta charset="utf-8">
<title>Quillridge Acres – Letterhead</title>
<link href="https://fonts.googleapis.com/css2?family=Montserrat:wght@600&family=Roboto:wght@400;500;700&display=swap" rel="stylesheet">
<style>
  :root {
    --forest: #465d2e;
    --leaf: #8dc63f;
    --leaf-soft: #a9d85a;
    --paper: #ffffff;
    --ink: #222222;
    --muted: #666666;
    --bg-a: #c9f56e;
    --bg-b: #e3f7c6;
  }
  * { margin: 0; padding: 0; box-sizing: border-box; }
  html, body { width: 1200px; height: 1000px; overflow: hidden; }
  body {
    background: linear-gradient(135deg, var(--bg-a) 0%, var(--bg-b) 100%);
    font-family: "Roboto", Arial, sans-serif;
    position: relative;
    color: var(--ink);
  }
  .sheet {
    position: absolute;
    top: 150px;
    width: 497px;
    height: 700px;
    box-shadow: 0 4px 14px rgba(40, 60, 20, 0.25);
  }
  .letter { left: 93px; background: var(--paper); }
  .cover { left: 610px; width: 495px; background: var(--forest); overflow: hidden; }

  .letter-frame { position: absolute; inset: 0; }

  .brand { position: absolute; left: 61px; top: 60px; display: flex; align-items: center; gap: 10px; }
  .brand-dot { width: 34px; height: 34px; border-radius: 50%; background: var(--forest); }
  .brand-name {
    font-family: "Montserrat", Arial, sans-serif; font-weight: 600; color: var(--leaf);
    line-height: 1;
  }
  .brand-name .line-1 { display: block; font-size: 21px; letter-spacing: 0.5px; }
  .brand-name .line-2 { display: block; font-size: 9px; letter-spacing: 3.2px; margin-top: 3px; }

  .recipient { position: absolute; left: 61px; top: 117px; font-size: 10px; }
  .recipient .salutation { color: var(--ink); }
  .recipient .name { font-size: 12px; font-weight: 500; color: var(--forest); margin-top: 3px; }
  .recipient .role { color: var(--muted); margin-top: 2px; }
  .recipient .details { margin-top: 11px; font-size: 8.5px; line-height: 13.5px; }
  .recipient .details span { display: inline-block; width: 14px; }

  .date { position: absolute; right: 62px; top: 117px; font-size: 10px; }

  .signature { position: absolute; left: 61px; top: 551px; font-size: 8.5px; font-weight: 700; }
  .signature .name { color: var(--forest); }
  .signature .title { color: var(--ink); margin-top: 2px; }

  .contacts { position: absolute; right: 61px; top: 545px; list-style: none; }
  .contacts li {
    display: flex; align-items: center; justify-content: flex-end; gap: 9px;
    font-size: 8.5px; text-align: right; height: 22px; margin-bottom: 4px; line-height: 1.3;
  }
  .icon { width: 22px; height: 22px; border-radius: 50%; flex: none; display: flex; align-items: center; justify-content: center; }
  .icon.leaf { background: var(--leaf); }
  .icon.forest { background: var(--forest); }

  .cover-brand {
    position: absolute; right: 28px; top: 24px; text-align: right;
    font-family: "Montserrat", Arial, sans-serif; font-weight: 600; color: var(--leaf); line-height: 1;
  }
  .cover-brand .line-1 { display: block; font-size: 36px; letter-spacing: 1px; }
  .cover-brand .line-2 { display: block; font-size: 15px; letter-spacing: 4px; margin-top: 6px; }

  .cover-pattern {
    position: absolute; left: 0; right: 0; top: 395px; bottom: 0;
    background: linear-gradient(180deg, #55703a 0%, #5f7d40 100%);
  }
</style>
</head>
<body>

<section class="sheet letter">
  <svg class="letter-frame" viewBox="0 0 497 700" width="497" height="700" aria-hidden="true">
    <polygon points="172,0 212,0 224,13 184,13" fill="var(--forest)"/>
    <polygon points="235,0 497,0 497,13 248,13" fill="var(--leaf)"/>
    <polygon points="482,13 497,13 497,408 482,396" fill="var(--leaf)"/>
    <polygon points="482,418 497,430 497,490 482,490" fill="var(--forest)"/>
    <polygon points="0,210 14,222 14,272 0,272" fill="var(--leaf)"/>
    <polygon points="0,288 14,300 14,685 0,685" fill="var(--forest)"/>
    <polygon points="0,685 257,685 272,700 0,700" fill="var(--forest)"/>
    <polygon points="272,685 310,685 325,700 287,700" fill="var(--leaf)"/>
  </svg>

  <div class="brand">
    <div class="brand-dot"></div>
    <div class="brand-name"><span class="line-1">QUILLRIDGE</span><span class="line-2">ACRES</span></div>
  </div>

  <div class="recipient">
    <p class="salutation">To,</p>
    <p class="name">First Name, Last Name</p>
    <p class="role">Executive Manager</p>
    <p class="details">
      <span>P</span>866-402-ACRE<br>
      <span>E</span>info@quillridgeacres.example<br>
      <span>A</span>Dallas, TX 75219
    </p>
  </div>

  <p class="date">Date: 20 August, 2020</p>

  <div class="signature">
    <p class="name">First Name, Last Name</p>
    <p class="title">CEO</p>
  </div>

  <ul class="contacts">
    <li>866-402-ACRE
      <span class="icon leaf"><svg width="12" height="12" viewBox="0 0 24 24"><path d="M6.6 10.8a15 15 0 0 0 6.6 6.6l2.2-2.2a1 1 0 0 1 1-.25 11.4 11.4 0 0 0 3.6.57 1 1 0 0 1 1 1V20a1 1 0 0 1-1 1A17 17 0 0 1 3 4a1 1 0 0 1 1-1h3.5a1 1 0 0 1 1 1c0 1.25.2 2.45.57 3.6a1 1 0 0 1-.25 1z" fill="#fff"/></svg></span>
    </li>
    <li>info@quillridgeacres.example
      <span class="icon forest"><svg width="12" height="12" viewBox="0 0 24 24" fill="none" stroke="#fff" stroke-width="2"><rect x="3" y="5" width="18" height="14" rx="1"/><path d="M3 6l9 7 9-7"/></svg></span>
    </li>
    <li><span>415 Bramwell Avenue #600<br>Dallas, TX 75219</span>
      <span class="icon leaf"><svg width="12" height="12" viewBox="0 0 24 24"><path d="M21 3L3 11l8 2 2 8z" fill="#fff"/></svg></span>
    </li>
    <li>www.quillridgeacres.example
      <span class="icon forest"><svg width="13" height="13" viewBox="0 0 24 24" fill="none" stroke="#fff" stroke-width="1.8"><circle cx="12" cy="12" r="9"/><ellipse cx="12" cy="12" rx="4" ry="9"/><path d="M3 12h18M5 7h14M5 17h14"/></svg></span>
    </li>
  </ul>
</section>

<section class="sheet cover">
  <div class="cover-brand"><span class="line-1">QUILLRIDGE</span><span class="line-2">ACRES</span></div>
  <div class="cover-pattern" role="img" aria-label="Repeating pattern of flying birds in white and light green"></div>
</section>

</body>
</html>
```